Hello,
Just to let you know this is urgent, please.

We are needing an A5 Advertisement for the back page of a calendar booklet. We need it to look sharp and elegant.
To keep it simple we would like to use logo as the graphic.
Attached below is the copy and a dropbox link for a selection of logos and the brand guidelines.
I look forward to receiving your designs.
Many thanks
Marjorie

```html
<!DOCTYPE html>
<html lang="en">
<head>
<meta charset="utf-8">
<title>Harbour Polo Club – April Cups Advertisement</title>
<link href="https://fonts.googleapis.com/css2?family=Bebas+Neue&family=Oswald:wght@200;300&family=Open+Sans:wght@600&display=swap" rel="stylesheet">
<style>
  :root {
    --gold: #c98f2e;
    --black: #111111;
    --white: #ffffff;
    --silver: #8a8a8c;
    --silver-light: #b9b9bb;
    --backdrop: #c4c5c8;
  }
  * { margin: 0; padding: 0; box-sizing: border-box; }
  html, body {
    width: 1200px; height: 1199px; overflow: hidden;
    background: var(--backdrop);
  }
  .advert-frame {
    position: absolute; left: 210px; top: 50px;
    width: 904px; height: 1276px;
    transform: scale(0.862); transform-origin: top left;
  }
  .advert {
    position: relative; width: 904px; height: 1276px;
    background: var(--white); overflow: hidden;
    font-family: "Bebas Neue", sans-serif; color: var(--black);
  }
  .abs { position: absolute; }
  .top-arc { left: 0; top: 0; }

  .club-mark { left: 0; top: 70px; width: 904px; text-align: center; }
  .club-mark .disc {
    width: 150px; height: 150px; border-radius: 50%;
    background: var(--black); margin: 0 auto 60px;
  }
  .club-mark .club-name {
    font-family: "Open Sans", sans-serif; font-weight: 600;
    font-size: 44px; letter-spacing: -0.5px; line-height: 1;
  }
  .club-mark .since {
    font-family: "Open Sans", sans-serif; font-weight: 600;
    font-size: 20px; margin-top: 8px;
  }

  .event { left: 31px; width: 860px; height: 156px; }
  .event .frame {
    position: absolute; left: 0; top: 0; width: 300px; height: 156px;
    border: 1.5px solid var(--silver);
  }
  .event .city { position: absolute; left: 15px; top: 6px; font-size: 72px; line-height: 1; }
  .event .cup {
    position: absolute; left: 15px; top: 72px;
    font-family: "Oswald", sans-serif; font-weight: 200;
    font-size: 62px; line-height: 1; letter-spacing: -1px; transform: scaleX(0.82); transform-origin: left;
  }
  .event .month-tab {
    position: absolute; left: 283px; top: 0; width: 138px; height: 63px;
    border-radius: 0 8px 8px 0; color: var(--white);
    font-size: 54px; line-height: 66px; text-align: center;
  }
  .event .mini-mark {
    position: absolute; left: 300px; top: 78px; width: 120px; text-align: center;
    font-family: "Open Sans", sans-serif; font-weight: 600; font-size: 10px;
  }
  .event .mini-mark .dot { width: 40px; height: 40px; border-radius: 50%; margin: 0 auto 8px; }
  .event .dates { position: absolute; left: 434px; top: 2px; font-size: 62px; line-height: 1; white-space: nowrap; }
  .event .year { position: absolute; left: 437px; top: 58px; font-size: 54px; line-height: 1; }
  .event .grades {
    position: absolute; left: 432px; top: 112px;
    font-family: "Oswald", sans-serif; font-weight: 300; font-size: 38px; line-height: 1;
    white-space: nowrap; transform: scaleX(0.78); transform-origin: left;
  }

  .event--silver { top: 425px; }
  .event--silver .cup, .event--silver .mini-mark { color: var(--silver-light); }
  .event--silver .month-tab, .event--silver .mini-mark .dot { background: var(--silver); }
  .event--silver .year { color: var(--silver); }

  .event--gold { top: 626px; }
  .event--gold .frame { border-color: var(--gold); }
  .event--gold .cup, .event--gold .year, .event--gold .mini-mark { color: var(--gold); }
  .event--gold .month-tab, .event--gold .mini-mark .dot { background: var(--gold); }
  .event--gold .dates { font-size: 56px; top: 6px; }

  .membership-band { left: 0; top: 817px; width: 904px; height: 201px; background: var(--black); }
  .membership-band .headline {
    position: absolute; left: 42px; top: 30px; color: var(--gold);
    font-size: 66px; line-height: 1; white-space: nowrap;
  }
  .membership-band .sub {
    position: absolute; left: 42px; top: 92px; color: var(--white);
    font-family: "Oswald", sans-serif; font-weight: 200; font-size: 60px; line-height: 1;
    transform: scaleX(0.8); transform-origin: left;
  }

  .accent-disc {
    left: 600px; top: 880px; width: 560px; height: 560px; border-radius: 50%;
    background: var(--gold);
  }

  .contact { left: 32px; top: 1036px; }
  .contact .label {
    color: var(--gold); font-family: "Oswald", sans-serif; font-weight: 300;
    font-size: 34px; line-height: 1; transform: scaleX(0.78); transform-origin: left;
  }
  .contact .phone { font-size: 78px; line-height: 1; margin-top: 12px; }
  .contact .address { font-size: 25px; line-height: 1; margin-top: 22px; white-space: nowrap; letter-spacing: 0.5px; }
  .contact .address .sep { margin: 0 18px; }
  .contact .web { font-size: 25px; line-height: 1; margin-top: 20px; letter-spacing: 22px; }
</style>
</head>
<body>
<div class="advert-frame">
  <div class="advert">
    <svg class="abs top-arc" width="904" height="160" viewBox="0 0 904 160" aria-hidden="true">
      <path d="M0 110 Q452 -60 904 110 L904 140 Q452 -20 0 140 Z" fill="var(--gold)"/>
    </svg>

    <div class="abs club-mark">
      <div class="disc"></div>
      <div class="club-name">HARBOUR POLO CLUB</div>
      <div class="since">SINCE 1870</div>
    </div>

    <section class="abs event event--silver">
      <div class="frame"></div>
      <div class="city">HARBOUR</div>
      <div class="cup">SILVER CUP</div>
      <div class="month-tab">APRIL</div>
      <div class="mini-mark"><div class="dot"></div>HARBOUR POLO CLUB</div>
      <div class="dates">11TH, 13TH &amp; 14TH</div>
      <div class="year">2019</div>
      <div class="grades">12, 6 AND 2 GOAL AND SUB ZERO</div>
    </section>

    <section class="abs event event--gold">
      <div class="frame"></div>
      <div class="city">HARBOUR</div>
      <div class="cup">GOLD CUP</div>
      <div class="month-tab">APRIL</div>
      <div class="mini-mark"><div class="dot"></div>HARBOUR POLO CLUB</div>
      <div class="dates">16TH, 17TH, 19TH &amp; 20TH</div>
      <div class="year">2019</div>
      <div class="grades">12, 6 AND 2 GOAL AND SUB ZERO</div>
    </section>

    <section class="abs membership-band">
      <div class="headline">PLAYING AND SOCIAL MEMBERSHIPS</div>
      <div class="sub">NOW AVAILABLE</div>
    </section>

    <div class="abs accent-disc" aria-hidden="true"></div>

    <section class="abs contact">
      <div class="label">HARBOUR POLO CLUB</div>
      <div class="phone">(02) 5550 1234</div>
      <div class="address">24 PADDOCK LANE KURRAJONG, NSW<span class="sep">|</span>ADMIN@HARBOURPOLO.COM</div>
      <div class="web">WWW.HARBOURPOLO.COM</div>
    </section>
  </div>
</div>
</body>
</html>
```